Quillmarrowhub.com Website Design

We would like to redesign quillmarowhub.com and we are looking for creative ideas. The new design should be clean and not resemble with any other existing website design.

The most important factor is that website have many banners/advertisements so the new design should be able to accommodate these banners of different size (Advertisement Friendly Design)

All Tools should be categorized under different main categories like all those tools that are related to content/writing will be shown under Content Tools ( Please find all categories and tools in attached file with the project). Right now all tools are showing randomly.

Also, Design single tool pages with sidebar, advertisement, and content placement.
ex. quillmarrowhub.com/plagiarism-checker/
quillmarrowhub.com/keyword-position/

Winning designer will also make the logo as well.

Target Market(s)

SEO Agencies, SEO executive, Article writers, Essay Writers, Plagiarism Checkers, Webmasters

Industry/Entity Type

Seo

Logo Text

Quill Marrow Hub

Number of Pages Required

5+ page

Font styles to use
Serif
Sans Serif
Other font styles liked:
• Any

Colors

Designer to choose colors to be used in the design.

Requirements
Must have
• 1) Clean Design
• 2) Modern Look
• 3) Easy To Navigate
• 4) Separate Icon for every Tool
• 5) Advertisement/Banners Freindly Design
Nice to have
• Matching Logo
• WOW Factor
Should not have
• Complex Design
• No drop down menu

```html
<!DOCTYPE html>
<html lang="en">
<head>
<meta charset="utf-8">
<title>Quill Marrow Hub – Free Online SEO Tools</title>
<link href="https://fonts.googleapis.com/css2?family=Roboto:wght@400;500;700&family=Open+Sans:wght@400;600&family=Montserrat:wght@500;600&family=Raleway:wght@400&display=swap" rel="stylesheet">
<style>
:root{
  --topbar:#2b4c9e;
  --navy:#1e3a56;
  --green:#1f8a3e;
  --btn-green:#3c9341;
  --red:#ee5a5a;
  --blue:#2e5aa8;
  --teal:#3da66b;
  --bg:#f2f2f2;
  --text:#333;
  --muted:#666;
  --line:#e6e6e6;
}
*{box-sizing:border-box;margin:0;padding:0}
html,body{width:932px;height:1200px;overflow:hidden}
body{position:relative;background:var(--bg);font-family:"Open Sans",sans-serif;color:var(--text)}
.abs{position:absolute}
.topbar{left:0;top:0;width:932px;height:24px;background:var(--topbar);color:#fff;font-family:"Roboto",sans-serif;font-size:9px}
.topbar .contact{left:78px;top:6px;display:flex;gap:12px;align-items:center}
.topbar .contact span{display:flex;align-items:center;gap:5px}
.topbar .social{left:710px;top:6px;display:flex;gap:8px;align-items:center}
.topbar .dot{width:8px;height:8px;border-radius:50%;background:#fff;opacity:.85}
.header{left:0;top:24px;width:932px;height:80px;background:#fff}
.brand{left:88px;top:28px;display:flex;align-items:center;gap:8px}
.brand .mark{width:22px;height:22px;border-radius:50%;background:var(--green)}
.brand .name{font-family:"Roboto",sans-serif;font-weight:700;font-size:22px;color:var(--topbar);line-height:1}
.tagline{left:130px;top:55px;font-family:"Roboto",sans-serif;font-weight:500;font-size:9px;letter-spacing:2px;color:var(--navy);line-height:1}
.cart{left:736px;top:32px}
.login{left:771px;top:26px;width:112px;height:32px;background:var(--btn-green);color:#fff;font-family:"Roboto",sans-serif;font-size:10px;display:flex}
.login .label{flex:1;display:flex;align-items:center;justify-content:center}
.login .lock{width:30px;background:#6aad64;display:flex;align-items:center;justify-content:center}
.nav{left:0;top:104px;width:932px;height:43px;background:#fff;border-top:1px solid var(--line);border-bottom:1px solid #ddd}
.nav a{position:absolute;top:14px;font-family:"Roboto",sans-serif;font-weight:500;font-size:11.5px;color:#222;text-decoration:none;letter-spacing:.3px}
.nav .active::before{content:"";position:absolute;left:-13px;top:-15px;width:57px;height:3px;background:var(--red)}
.search{left:645px;top:8px;width:239px;height:27px;background:#e8e8e8;display:flex;align-items:center;padding-left:7px}
.section-title{left:79px;top:186px;width:560px;text-align:center;font-family:"Roboto",sans-serif;font-weight:700;font-size:13px;color:#222}
.rule{top:193px;width:122px;height:3px;border-top:1px solid #ddd;border-bottom:1px solid #ddd}
.section-sub{left:79px;top:211px;width:560px;text-align:center;font-family:"Raleway",sans-serif;font-size:10.5px;color:#666}
.ad{background:linear-gradient(90deg,#0f4f8a 0%,#155c99 72%,#9bc23c 72%,#a8c83a 100%)}
.card{background:#fff;border:1px solid #e8e8e8;border-bottom-width:3px;width:178px}
.card.b-blue{border-bottom-color:var(--blue)}
.card.b-red{border-bottom-color:var(--red)}
.card.b-green{border-bottom-color:var(--teal)}
.card .ico{position:absolute;left:-13px;top:17px;width:26px;height:26px;border-radius:50%;display:flex;align-items:center;justify-content:center}
.ico.blue{background:var(--blue)}.ico.red{background:var(--red)}.ico.green{background:var(--teal)}
.card h3{position:absolute;left:21px;top:23px;font-family:"Roboto",sans-serif;font-weight:500;font-size:13px;color:#222}
.card ul{position:absolute;left:22px;top:50px;list-style:none;font-size:10px;line-height:22.6px;color:#555;letter-spacing:.2px;white-space:nowrap}
.sidebar{left:686px;top:174px;width:210px;height:948px;background:#fff}
.subscribe{left:696px;top:181px;width:190px;height:147px;background:var(--navy);color:#fff;overflow:hidden}
.subscribe h4{position:absolute;left:13px;top:22px;font-family:"Roboto",sans-serif;font-weight:500;font-size:14.5px}
.subscribe p{position:absolute;left:13px;top:53px;width:170px;font-family:"Roboto",sans-serif;font-size:8.5px;line-height:10.5px}
.subscribe .field{position:absolute;left:13px;top:95px;width:131px;height:27px;background:#fff}
.subscribe .go{position:absolute;left:144px;top:95px;width:31px;height:27px;background:var(--green);display:flex;align-items:center;justify-content:center}
.widget{left:696px;width:188px;background:#fff;border:1px solid #eee}
.widget h5{height:32px;background:var(--green);color:#fff;font-family:"Roboto",sans-serif;font-weight:500;font-size:11.5px;padding:10px 0 0 12px;letter-spacing:.3px}
.widget ul{list-style:none;font-family:"Montserrat",sans-serif;font-weight:500;font-size:9.5px;color:#222}
.widget li{height:31.5px;display:flex;align-items:center;gap:10px;padding-left:14px;border-bottom:1px solid #eee}
.widget li:last-child{border-bottom:0}
.readmore{left:330px;top:1095px;width:104px;height:27px;border-radius:14px;background:var(--navy);color:#fff;font-family:"Roboto",sans-serif;font-size:10px;display:flex;align-items:center;justify-content:center}
.footer{left:0;top:1160px;width:932px;height:40px;background:#dadada;font-family:"Open Sans",sans-serif;font-size:9.5px;color:#444;text-align:center;padding-top:14px}
</style>
</head>
<body>

<div class="abs topbar">
  <div class="abs contact">
    <span><svg width="10" height="8" viewBox="0 0 10 8"><rect x=".5" y=".5" width="9" height="7" fill="none" stroke="#fff"/><path d="M.5 .5 5 4.5 9.5 .5" fill="none" stroke="#fff"/></svg>hello@fernwick-studio.com</span>
    <span><svg width="9" height="9" viewBox="0 0 9 9"><rect width="9" height="9" rx="2" fill="#fff"/><path d="M2.5 2c.5 2 2 3.8 4 4.5l.5-1" stroke="#2b4c9e" fill="none"/></svg>+555 014 372</span>
    <span><svg width="9" height="9" viewBox="0 0 9 9"><circle cx="4.5" cy="4.5" r="4" fill="#fff"/></svg>chat4support</span>
  </div>
  <div class="abs social">
    <span style="margin-right:6px">Connect with us</span>
    <i class="dot"></i><i class="dot"></i><i class="dot"></i><i class="dot"></i><i class="dot"></i><i class="dot"></i>
  </div>
</div>

<header class="abs header">
  <div class="abs brand">
    <i class="mark"></i><span class="name">Quill Marrow Hub</span>
  </div>
  <div class="abs tagline">Free Online SEO Tools</div>
  <svg class="abs cart" width="22" height="20" viewBox="0 0 22 20">
    <path d="M1 3h3l2.5 9h10l2-6.5H6" fill="none" stroke="#333" stroke-width="1.5"/>
    <circle cx="8" cy="16" r="1.5" fill="#333"/><circle cx="15" cy="16" r="1.5" fill="#333"/>
    <circle cx="18" cy="4" r="3.5" fill="#ee5a5a"/>
  </svg>
  <div class="abs login">
    <span class="label">Login / Register</span>
    <span class="lock"><svg width="9" height="11" viewBox="0 0 9 11"><rect x="1" y="5" width="7" height="5.5" fill="none" stroke="#fff"/><path d="M2.5 5V3a2 2 0 0 1 4 0v2" fill="none" stroke="#fff"/></svg></span>
  </div>
</header>

<nav class="abs nav">
  <a class="active" style="left:93px">HOME</a>
  <a style="left:162px">PLAGIARISM CHECKER</a>
  <a style="left:322px">ADVERTISE</a>
  <a style="left:419px">BLOG</a>
  <a style="left:486px">CONTACT US</a>
  <div class="abs search"><svg width="14" height="14" viewBox="0 0 14 14"><circle cx="6" cy="6" r="4.5" fill="none" stroke="#111" stroke-width="2"/><path d="M9.5 9.5 13 13" stroke="#111" stroke-width="2"/></svg></div>
</nav>

<div class="abs rule" style="left:87px"></div>
<div class="abs rule" style="left:508px"></div>
<h2 class="abs section-title">SEARCH ENGINE OPTIMIZATION TOOLS</h2>
<p class="abs section-sub">Find out &amp; explore new businesses near your area and see what's happening !!!</p>

<div class="abs ad" style="left:118px;top:258px;width:484px;height:59px" role="img" aria-label="Advertisement banner for a regional earthquake drill event"></div>

<section class="abs card b-blue" style="left:79px;top:362px;height:264px">
  <span class="ico blue"><svg width="12" height="12" viewBox="0 0 12 12"><path d="M2 2l8 8M10 2 2 10" stroke="#fff" stroke-width="1.6"/></svg></span>
  <h3>Content Tools</h3>
  <ul><li>Plagiarism Checker</li><li>Article Rewriter</li><li>Grammar Checker</li><li>Word Count Checker</li><li>Spell Checker</li><li>Online MD5 Generator</li><li>Change Text Case</li><li>Merge Words Online Tool</li><li>Image to Text Converter</li></ul>
</section>
<section class="abs card b-green" style="left:79px;top:654px;height:215px">
  <span class="ico green"><svg width="12" height="12" viewBox="0 0 12 12"><path d="M4 8 8 4M3 6a2.5 2.5 0 0 0 3 3M9 6a2.5 2.5 0 0 0-3-3" stroke="#fff" stroke-width="1.4" fill="none"/></svg></span>
  <h3>BackLink Tools</h3>
  <ul><li>Backlink Checker</li><li>Backlink Maker</li><li>Website Link Count Checker</li><li>Website Broken Link Checker</li><li>Link Price Calculator</li><li>Reciprocal Link Checker</li><li>Website Link Analyzer Tool</li></ul>
</section>
<section class="abs card b-blue" style="left:79px;top:902px;height:136px">
  <span class="ico blue"><svg width="10" height="12" viewBox="0 0 10 12"><path d="M1 1h5.5L9 3.5V11H1z" fill="#fff"/></svg></span>
  <h3>Proxy Tools</h3>
  <ul><li>What is My IP</li><li>IP Location</li><li>Free Daily Proxy List</li></ul>
</section>

<section class="abs card b-red" style="left:285px;top:362px;height:214px">
  <span class="ico red"><svg width="12" height="12" viewBox="0 0 12 12"><path d="M2 10 7 5M7 5a2.5 2.5 0 1 0 0-.1" stroke="#fff" stroke-width="1.5" fill="none"/></svg></span>
  <h3>Images Handling Tools</h3>
  <ul><li>Reverse Image Search</li><li>Image Compression</li><li>Favicon Generator Tool</li><li>Video to GIF Converter</li><li>Image Resizer</li><li>Crop Image</li><li>Convert to JPG</li></ul>
</section>
<section class="abs card b-blue" style="left:285px;top:608px;height:262px">
  <span class="ico blue"><svg width="12" height="12" viewBox="0 0 12 12"><circle cx="6" cy="6" r="5" fill="none" stroke="#fff"/><path d="M1 6h10M6 1c-3 3-3 7 0 10M6 1c3 3 3 7 0 10" stroke="#fff" fill="none"/></svg></span>
  <h3>Domains Tools</h3>
  <ul><li>Domain Age Checker</li><li>Domain Authority Checker</li><li>Domain Ip Lookup</li><li>Domain Hosting Checker</li><li>Find DNS records</li><li>Domain Name Checker</li><li>Domain to IP</li><li>Blacklist Lookup</li><li>Expired Domains Too</li></ul>
</section>
<section class="abs card b-red" style="left:285px;top:904px;height:134px">
  <span class="ico red"><svg width="10" height="12" viewBox="0 0 10 12"><path d="M1 1h5.5L9 3.5V11H1z" fill="#fff"/></svg></span>
  <h3>Password Tools</h3>
  <ul><li>Password Encryption Utility</li><li>Password Strength Checker</li><li>Password Generator</li></ul>
</section>

<section class="abs card b-green" style="left:494px;top:362px;height:304px">
  <span class="ico green"><svg width="12" height="12" viewBox="0 0 12 12"><circle cx="5" cy="5" r="3.5" fill="none" stroke="#fff" stroke-width="1.5"/><path d="M7.5 7.5 11 11" stroke="#fff" stroke-width="1.6"/></svg></span>
  <h3>Keywords Tools</h3>
  <ul style="font-size:9.6px"><li>Images Handling Tool</li><li>Keyword Position</li><li>Keywords Density Checker</li><li>Keywords Suggestions Tool</li><li>Website Keywords Suggestions</li><li>keywords Domains Suggestions</li><li>Related keywords Finder</li><li>Long Tail Keyword Suggestion</li><li>Keyword Competition Checker</li><li>Keyword Competition Analysis</li><li>Live Keyword Analyzer</li></ul>
</section>
<section class="abs card b-red" style="left:494px;top:692px;height:262px">
  <span class="ico red"><svg width="10" height="12" viewBox="0 0 10 12"><path d="M1 1h5.5L9 3.5V11H1z" fill="#fff"/></svg></span>
  <h3>PDF Tools</h3>
  <ul><li>Merge PDF</li><li>Rotate PDF</li><li>Unlock PDF</li><li>Lock PDF</li><li>Watermark</li><li>Word to Pdf</li><li>Pdf to Jpg</li><li>Jpg to Pdf</li><li>Slideshow to Pdf</li></ul>
</section>
<section class="abs card b-green" style="left:494px;top:982px;height:101px">
  <span class="ico green"><svg width="10" height="12" viewBox="0 0 10 12"><path d="M1 1h5.5L9 3.5V11H1z" fill="#fff"/></svg></span>
  <h3>Meta Tools</h3>
  <ul><li>Meta Tags Analyzer</li><li>Meta Tag Generator</li></ul>
</section>

<div class="abs readmore">Read More ›</div>

<aside class="abs sidebar"></aside>
<div class="abs subscribe">
  <h4>Subscribe Now!</h4>
  <p>Quill Marrow Hub is one of the biggest free SEO tools provider.</p>
  <div class="field"></div>
  <div class="go"><svg width="13" height="9" viewBox="0 0 13 9"><path d="M0 4.5h11M8 1l3.5 3.5L8 8" stroke="#fff" stroke-width="1.4" fill="none"/></svg></div>
</div>
<div class="abs" style="left:696px;top:352px;width:190px;height:159px;background:linear-gradient(135deg,#1f4fb8 0%,#2a62d0 60%,#3b8fd8 100%)" role="img" aria-label="Advertisement for a cloud integration platform analyst report"></div>

<div class="abs widget" style="top:534px">
  <h5>IMAGES HANDLING TOOL</h5>
  <ul>
    <li><svg width="12" height="12" viewBox="0 0 12 12"><circle cx="5" cy="5" r="3.5" fill="none" stroke="#333" stroke-width="1.4"/><path d="M7.5 7.5 11 11" stroke="#333" stroke-width="1.5"/></svg>Reverse image Search</li>
    <li><svg width="13" height="11" viewBox="0 0 13 11"><rect x=".5" y=".5" width="12" height="10" fill="none" stroke="#333"/><path d="M1 10 5 5l3 3 2-2 2.5 4" fill="#333"/></svg>Video to gif Coverter</li>
    <li><svg width="13" height="11" viewBox="0 0 13 11"><rect x=".5" y="2" width="12" height="8.5" rx="1.5" fill="#333"/><circle cx="6.5" cy="6.2" r="2.3" fill="#fff"/></svg>Convert to JPG</li>
    <li><svg width="13" height="11" viewBox="0 0 13 11"><rect x=".5" y=".5" width="12" height="10" fill="#333"/><path d="M1.5 9.5 5 5l2.5 3 2-2 2 3.5z" fill="#fff"/></svg>Image Compression</li>
    <li><svg width="13" height="11" viewBox="0 0 13 11"><rect x=".5" y=".5" width="12" height="10" fill="none" stroke="#333"/><path d="M1 10 5 4l3 4 2-2 2.5 4z" fill="#333"/></svg>Favicon Genrator</li>
    <li><svg width="12" height="12" viewBox="0 0 12 12"><path d="M1 4V1h3M8 1h3v3M11 8v3H8M4 11H1V8" stroke="#333" stroke-width="1.4" fill="none"/><rect x="3.5" y="3.5" width="5" height="5" fill="#333"/></svg>Image Resizer</li>
    <li><svg width="12" height="12" viewBox="0 0 12 12"><path d="M3 0v9h9M0 3h9v9" stroke="#333" stroke-width="1.5" fill="none"/></svg>Crop image</li>
  </ul>
</div>

<div class="abs widget" style="top:818px">
  <h5>PROXY TOOLS</h5>
  <ul>
    <li><svg width="12" height="12" viewBox="0 0 12 12"><circle cx="5" cy="5" r="3.5" fill="none" stroke="#333" stroke-width="1.4"/><path d="M7.5 7.5 11 11" stroke="#333" stroke-width="1.5"/></svg>what is my Ip</li>
    <li><svg width="13" height="11" viewBox="0 0 13 11"><rect x=".5" y=".5" width="12" height="10" fill="none" stroke="#333"/><path d="M1 10 5 5l3 3 2-2 2.5 4" fill="#333"/></svg>Ip Location</li>
    <li><svg width="13" height="11" viewBox="0 0 13 11"><rect x=".5" y="2" width="12" height="8.5" rx="1.5" fill="#333"/><circle cx="6.5" cy="6.2" r="2.3" fill="#fff"/></svg>Free Daily Proxy List</li>
  </ul>
</div>

<div class="abs widget" style="top:974px">
  <h5>META TOOLS</h5>
  <ul>
    <li><svg width="12" height="12" viewBox="0 0 12 12"><circle cx="5" cy="5" r="3.5" fill="none" stroke="#333" stroke-width="1.4"/><path d="M7.5 7.5 11 11" stroke="#333" stroke-width="1.5"/></svg>Meta Tags Analyzer</li>
    <li><svg width="13" height="11" viewBox="0 0 13 11"><rect x=".5" y=".5" width="12" height="10" fill="none" stroke="#333"/><path d="M1 10 5 5l3 3 2-2 2.5 4" fill="#333"/></svg>Meta tag Generator</li>
  </ul>
</div>

<footer class="abs footer">Copyright © 2012-2017 by Quillmarrowhub.com. All Rights Reserved.</footer>

</body>
</html>
```